Business Cards

Business cards (double-sided) to be handed out to clients and potential clients, with contact details, logo .

Target Market(s)

Small to medium size businesses

Industry/Entity Type

Accountants

Contact Information for Business Card

Brightwater Ledger & Counsel Ltd

Colors

Designer to choose only greyscale colors for use in the design.

Requirements
Must have
• Name, Title, Address, Phone number, Email, Website
Nice to have
• Modern, clean lines, classy
Should not have
• Business cards to be double-sided. Form keeps reverting to single-sided.

```html
<!DOCTYPE html>
<html lang="en">
<head>
<meta charset="utf-8">
<title>Brightwater Ledger &amp; Counsel – Business Cards</title>
<link rel="stylesheet" href="https://fonts.googleapis.com/css2?family=Arimo:wght@400;700&display=swap">
<style>
  :root {
    --backdrop: #e4e4e4;
    --card-dark: #3a3a3a;
    --card-light: #ffffff;
    --ink-dark: #2e2e2e;
    --ink-light: #f4f4f4;
    --line-light: #cfcfcf;
    --emboss: #4a4a4a;
    --emboss-edge: #2a2a2a;
  }
  * { box-sizing: border-box; margin: 0; padding: 0; }
  html, body {
    width: 1200px; height: 802px; overflow: hidden;
    background: var(--backdrop);
    font-family: "Arimo", Arial, sans-serif;
  }
  .sheet {
    width: 1200px; height: 802px;
    display: flex; align-items: center; justify-content: center; gap: 60px;
  }
  .card {
    width: 525px; height: 300px;
    position: relative; overflow: hidden;
    box-shadow: 0 2px 6px rgba(0,0,0,.12);
  }

  /* Front side */
  .card--front { display: flex; }
  .front__brand {
    width: 50%; background: var(--card-light);
    display: flex; align-items: center; justify-content: center;
  }
  .brand-name {
    display: flex; align-items: center; gap: 10px;
    color: var(--ink-dark); font-weight: 400;
    font-size: 17px; letter-spacing: 1.5px; text-transform: uppercase; line-height: 1.3;
  }
  .brand-name__square { width: 12px; height: 12px; background: var(--ink-dark); flex: none; }

  .front__contact {
    width: 50%; background: var(--card-dark);
    display: flex; align-items: center; justify-content: center;
  }
  .contact-frame {
    position: relative; padding: 22px 22px 22px 26px; width: 218px;
    color: var(--ink-light);
  }
  .contact-frame::before, .contact-frame::after {
    content: ""; position: absolute; width: 70%; height: 70%;
  }
  .contact-frame::before {
    top: 0; left: 0;
    border-top: 1px solid var(--line-light); border-left: 1px solid var(--line-light);
  }
  .contact-frame::after {
    bottom: 0; right: 0;
    border-bottom: 1px solid var(--line-light); border-right: 1px solid var(--line-light);
  }
  .contact__name { font-weight: 700; font-size: 15px; letter-spacing: .5px; text-transform: uppercase; }
  .contact__title { font-size: 12px; margin-bottom: 12px; }
  .contact__address { font-size: 12px; line-height: 1.35; margin-bottom: 12px; }
  .contact__list { list-style: none; font-size: 11.5px; line-height: 1.6; }
  .contact__list li { display: flex; align-items: center; gap: 7px; }
  .contact__list svg { width: 11px; height: 11px; flex: none; }

  /* Back side */
  .card--back {
    background: var(--card-dark);
    display: flex; align-items: center; justify-content: center;
  }
  .brand-name--emboss {
    color: var(--emboss); font-size: 22px; letter-spacing: 2px;
    text-shadow: 0 -1px 0 var(--emboss-edge);
  }
  .brand-name--emboss .brand-name__square { background: var(--emboss); width: 15px; height: 15px; }
</style>
</head>
<body>
<main class="sheet">
  <section class="card card--front" aria-label="Business card front">
    <div class="front__brand">
      <p class="brand-name"><span class="brand-name__square"></span><span>Brightwater Ledger<br>&amp; Counsel</span></p>
    </div>
    <div class="front__contact">
      <div class="contact-frame">
        <h1 class="contact__name">Daniel Harrow</h1>
        <p class="contact__title">Manager</p>
        <p class="contact__address">Your Address, City<br>State, Zip 0000</p>
        <ul class="contact__list">
          <li><svg viewBox="0 0 12 12" aria-hidden="true"><circle cx="6" cy="6" r="6" fill="#f4f4f4"/><path d="M4 3.2l1 .2.4 1.4-.7.5c.4.9 1 1.5 1.9 1.9l.5-.7 1.4.4.2 1c-.5.6-1.3.8-2 .5C5 7.8 4.2 7 3.6 5.4c-.3-.8-.1-1.6.4-2.2z" fill="#3a3a3a"/></svg>555-014-2288</li>
          <li><svg viewBox="0 0 12 12" aria-hidden="true"><rect x="0.5" y="2" width="11" height="8" fill="#f4f4f4"/><path d="M1 2.5l5 4 5-4" fill="none" stroke="#3a3a3a" stroke-width="1"/></svg>hello@brightwaterledger.com</li>
          <li><svg viewBox="0 0 12 12" aria-hidden="true"><circle cx="6" cy="6" r="5.5" fill="#f4f4f4"/><path d="M.5 6h11M6 .5c-2.5 3-2.5 8 0 11M6 .5c2.5 3 2.5 8 0 11" fill="none" stroke="#3a3a3a" stroke-width=".8"/></svg>www.brightwaterledger.com</li>
        </ul>
      </div>
    </div>
  </section>

  <section class="card card--back" aria-label="Business card back">
    <p class="brand-name brand-name--emboss"><span class="brand-name__square"></span><span>Brightwater Ledger<br>&amp; Counsel</span></p>
  </section>
</main>
</body>
</html>
```